Very Simple Web Redesign Project - Using Photoshop

Required is a very simple website home page redesign for the following site: http://www.tallowcrestslate.com.au/
I require this as a Photoshop design.
The basic look and feel of the site needs to remain.
Specifically the colours don't need to be changed.
The positioning of the site is currently correct for the target market.
The site does not need to be made super slick looking. Just upgraded to a new version.
The current text can all be used.
The only menus necessary are a horizontal menu at the top, and a simple horizontal text menu at the bottom of the page. Do NOT retain the vertical menu on the home page (having the items "Our Gallery", "Our Services", "Enquire Now").
Give the horizontal menu the following items:
Home | Slate Roof Repairs | Slate Reroofing | Slate Roof Benefits | Other Services | Photo Gallery | FAQ's | Free Quote | Contact Us
The picture of the house at the top RHS of the page needs to be reduced in size by approx 50% and moved to the top LHS of the page.
Please place the following text into the top of the page:
"Call Now: 0427 618 392"
Keep the four pictures on the home page layout. Some larger images attached.
Thanks,
Rob
Updates
Hi,
Thanks for all the designs.
I am working with my client to get which one they like the most.
Thanks,
Rob

```html
<!DOCTYPE html>
<html lang="en">
<head>
<meta charset="utf-8">
<title>Tallowcrest Slate – The Slate Roof Specialists</title>
<link href="https://fonts.googleapis.com/css2?family=Crimson+Pro:wght@400;600;700&family=Open+Sans:wght@400;600;700&family=Archivo:wght@700&display=swap" rel="stylesheet">
<style>
  :root{
    --green-dark:#2f6e12;
    --green:#4a8a1f;
    --green-light:#8cc63f;
    --green-bright:#6ab02a;
    --green-text:#3b7a12;
    --ink:#111;
    --grey-text:#666;
    --grey-head:#777;
    --panel:#f4f6f2;
    --frame:#1b1b1b;
    --gallery-bg:#d9dad8;
    --white:#fff;
  }
  *{box-sizing:border-box;margin:0;padding:0}
  html,body{width:1069px;height:1200px;overflow:hidden;background:var(--white)}
  body{position:relative;font-family:"Crimson Pro",Georgia,serif;color:var(--grey-text)}

  .top-rule{position:absolute;left:0;top:0;width:1069px;height:6px;background:linear-gradient(#c8c8c8,#eee)}

  .site-header{position:absolute;left:0;top:6px;width:1069px;height:208px;overflow:hidden;
    background:linear-gradient(180deg,#4d8f22 0%,#3f811a 60%,#3b7c17 100%)}
  .site-header svg.swoosh{position:absolute;left:0;top:0}
  .brand{position:absolute;left:24px;top:78px;display:flex;align-items:center;gap:22px}
  .brand-mark{width:90px;height:90px;background:#6a8f4a;border:2px solid #d9e7c9}
  .brand-name{font-family:"Crimson Pro",Georgia,serif;font-weight:600;font-size:52px;color:var(--white);letter-spacing:.3px}
  .header-phone{position:absolute;right:12px;top:118px;display:flex;align-items:center;gap:8px;
    font-family:"Open Sans",Arial,sans-serif;font-weight:600;font-size:23px;color:var(--white)}
  .phone-icon{width:25px;height:25px;border-radius:5px;background:var(--green-light);display:flex;align-items:center;justify-content:center}

  .main-nav{position:absolute;left:0;top:214px;width:1069px;height:48px;
    background:linear-gradient(#fff 0%,#f2f2f2 60%,#e4e4e4 100%);border-bottom:2px solid #d8d8d8}
  .main-nav ul{list-style:none;display:flex;align-items:center;height:46px;padding-left:19px;
    font-family:"Open Sans",Arial,sans-serif;font-size:13.4px;color:var(--ink)}
  .main-nav li+li::before{content:"|";margin:0 13px 0 13px;color:var(--ink)}
  .main-nav li.current{color:var(--green-text)}

  .content-frame{position:absolute;left:0;top:263px;width:1069px;height:828px;background:var(--frame)}
  .content-panel{position:absolute;left:12px;top:11px;width:1046px;height:797px;background:var(--panel)}

  .gallery{position:absolute;left:9px;top:8px;width:1030px;height:389px;background:var(--gallery-bg);
    box-shadow:0 1px 3px rgba(0,0,0,.25)}
  .photo{position:absolute;border:4px solid var(--white);outline:1px solid #bbb}
  .photo-a{left:11px;top:13px;width:274px;height:357px;background:linear-gradient(160deg,#9cb8d0 0%,#6f7a84 35%,#4c545c 65%,#c9c6bd 100%)}
  .photo-b{left:295px;top:13px;width:275px;height:357px;background:linear-gradient(170deg,#b9a89a 0%,#7d7a74 40%,#5f625f 70%,#8a6e58 100%)}
  .photo-c{left:580px;top:13px;width:440px;height:175px;background:linear-gradient(120deg,#7a6f67 0%,#4a4c55 45%,#d9cfa8 70%,#7b6f60 100%)}
  .photo-d{left:580px;top:195px;width:440px;height:175px;background:linear-gradient(160deg,#d8ccaa 0%,#6c6c6c 40%,#4f5458 70%,#b98e6c 100%)}

  .intro{position:absolute;left:20px;top:430px;width:680px}
  .intro h1{font-family:"Archivo",Arial,sans-serif;font-weight:700;font-size:20px;color:var(--grey-head);margin-bottom:14px;letter-spacing:.1px}
  .intro h1 span{color:var(--green-text)}
  .intro p{font-size:15.6px;line-height:19px;color:var(--grey-text);margin-bottom:19px}
  .intro a{color:#1a3fd6;text-decoration:underline}

  .quote-box{position:absolute;left:740px;top:432px;width:280px;height:303px;
    background:linear-gradient(#fff,#f4f4f4);box-shadow:0 0 4px rgba(0,0,0,.35)}
  .quote-box h2{margin:6px 6px 0;height:40px;background:linear-gradient(#8fd03a,#5ea81c);
    font-family:"Archivo",Arial,sans-serif;font-weight:700;font-size:20px;color:var(--white);
    display:flex;align-items:center;padding-left:12px;border:1px solid #4d8f18}
  .quote-box h2 span{color:var(--ink);margin-left:6px}
  .quote-body{padding:8px 12px 0 12px;font-size:15px;line-height:19px;color:var(--grey-text);height:178px}
  .quote-mark{float:left;width:96px;height:96px;margin:0 8px 4px 0;background:#7c8f6c}
  .quote-rule{margin:0 6px;border-top:1px solid #d6d6d6;border-bottom:1px solid #fff}
  .quote-phone{text-align:center;padding-top:14px;font-family:"Open Sans",Arial,sans-serif;font-weight:600;font-size:18px;color:var(--grey-head)}
  .quote-phone span{color:var(--green-bright);letter-spacing:1.5px;margin-left:4px}

  .site-footer{position:absolute;left:0;top:1092px;width:1069px;height:104px;
    background:linear-gradient(#2f6b12,#3e7e1a 40%,#4a8a22);border-top:2px solid #fff}
  .footer-nav{position:absolute;left:11px;top:34px;list-style:none;display:flex;
    font-family:"Open Sans",Arial,sans-serif;font-size:11px;color:var(--white)}
  .footer-nav li+li::before{content:"|";margin:0 10px}
  .footer-nav li.current{color:var(--ink)}
  .copyright{position:absolute;left:11px;top:54px;font-family:"Open Sans",Arial,sans-serif;font-size:11px;color:var(--white)}
  .business-ids{position:absolute;left:896px;top:30px;font-family:"Crimson Pro",Georgia,serif;font-weight:700;font-size:15px;line-height:19px;color:var(--white)}
</style>
</head>
<body>
  <div class="top-rule"></div>

  <header class="site-header">
    <svg class="swoosh" width="1069" height="208" viewBox="0 0 1069 208" aria-hidden="true">
      <defs>
        <linearGradient id="swooshFill" x1="0" y1="0" x2="1" y2="0">
          <stop offset="0" stop-color="#9cd143" stop-opacity=".9"/>
          <stop offset=".45" stop-color="#6aae2c" stop-opacity=".6"/>
          <stop offset="1" stop-color="#3d7e18" stop-opacity="0"/>
        </linearGradient>
      </defs>
      <path d="M0 60 C 200 30, 420 30, 620 70 C 760 100, 860 140, 1069 175 L1069 0 L0 0 Z" fill="#3a7a15"/>
      <path d="M0 70 C 200 35, 420 35, 620 75 C 760 105, 860 145, 1069 178 L1069 208 L0 208 Z" fill="url(#swooshFill)"/>
    </svg>
    <div class="brand">
      <div class="brand-mark"></div>
      <span class="brand-name">Tallowcrest Slate</span>
    </div>
    <div class="header-phone">
      <span class="phone-icon">
        <svg width="15" height="15" viewBox="0 0 24 24" aria-hidden="true"><path fill="#fff" d="M6.6 10.8c1.4 2.8 3.8 5.1 6.6 6.6l2.2-2.2c.3-.3.7-.4 1-.2 1.1.4 2.3.6 3.6.6.6 0 1 .4 1 1V20c0 .6-.4 1-1 1C10.6 21 3 13.4 3 4c0-.6.4-1 1-1h3.5c.6 0 1 .4 1 1 0 1.3.2 2.5.6 3.6.1.3 0 .7-.2 1z"/></svg>
      </span>
      0427 618 392
    </div>
  </header>

  <nav class="main-nav">
    <ul>
      <li class="current">Home</li>
      <li>Slate Roof Repairs</li>
      <li>Slate Reroofing</li>
      <li>Slate Roof Benefits</li>
      <li>Other Services</li>
      <li>Photo Gallery</li>
      <li>FAQ's</li>
      <li>Free Quote</li>
      <li>Contact Us</li>
    </ul>
  </nav>

  <main class="content-frame">
    <div class="content-panel">
      <section class="gallery">
        <div class="photo photo-a" role="img" aria-label="Slate roof on a period house with bay window"></div>
        <div class="photo photo-b" role="img" aria-label="Slate roof beside a brick house with balcony stairs"></div>
        <div class="photo photo-c" role="img" aria-label="Slate roof with a dormer window"></div>
        <div class="photo photo-d" role="img" aria-label="Close view of slate roof around a dormer window"></div>
      </section>

      <section class="intro">
        <h1>TALLOWCREST SLATE - <span>THE SLATE ROOF SPECIALISTS</span></h1>
        <p>At Tallowcrest Slate we specialize in the upkeep, maintenance, repair and replacement of all types of slate roof as well as wood shingles.&nbsp; We can track down the leak that just won't go away or give your house a complete re-roof. We can also provide all your guttering needs.</p>
        <p>Tallowcrest Slate is a small company and as such we do not have the overheads that larger companies do. Quality work and attention to detail are our trademark.</p>
        <p>All photos on this website consist of work which I have personally done.&nbsp; The above photos provide at a quick glance a reasonable cross section of the type of work I do.</p>
        <p>By clicking on the Photo Gallery link you can see other work including some before and after shots.</p>
        <p>Feel free to call at your earliest convenience to organise an obligation free quote or fill out a form by clicking on the <a href="#">Contact Us</a> link below.</p>
      </section>

      <aside class="quote-box">
        <h2>CALL FOR <span>FREE QUOTE</span></h2>
        <div class="quote-body">
          <div class="quote-mark"></div>
          We service all inner city suburbs of Sydney roughly covering an area encompassing Gordon to Epping, Mosman to Bondi, Coogee to Kogarah and Kingsgrove to Burwood and
        </div>
        <div class="quote-rule"></div>
        <div class="quote-phone">Phone : <span>0427 618 392</span></div>
      </aside>
    </div>
  </main>

  <footer class="site-footer">
    <ul class="footer-nav">
      <li class="current">Home</li>
      <li>Slate Roof Repairs</li>
      <li>Slate Reroofing</li>
      <li>Slate Roof Benefits</li>
      <li>Other Services</li>
      <li>Photo Gallery</li>
      <li>FAQ's</li>
      <li>Free Quote</li>
      <li>Contact Us</li>
    </ul>
    <div class="copyright">© All Rights Reserved</div>
    <div class="business-ids">ABN 47 309 218 665<br>Lic No. 204715C</div>
  </footer>
</body>
</html>
```